Yearbook of one of our programs

Our company, Meridian Ascent, www.meridianascent.example, hosts leadership programs and workshops for women in leadership roles from different companies all around the world. We need a year book, 11 x 17 inches, we will print with a soft cover, and be approximately 70 pages. Due date for the final completion is 12/9. However, the initial contest & fee is only for pages 1-5, 26-27 and 40-41 (please see attached last year's version). We’d like to use the same color as that. Also attached is the outline we will use once a designer is selected. $50 hourly rate for the completion of the book is set once a designer is confirmed.

```html
<!DOCTYPE html>
<html lang="en">
<head>
<meta charset="utf-8">
<title>Meridian Ascent Yearbook Cover</title>
<link href="https://fonts.googleapis.com/css2?family=Lato:wght@400;700;900&family=Caveat:wght@500&display=swap" rel="stylesheet">
<style>
  :root {
    --magenta: #b10d3e;
    --pink-band: #dc7299;
    --paper: #f1ebee;
    --paper-light: #f6f2f4;
    --numeral: #ecd2dc;
    --backdrop: #cacaca;
    --white: #ffffff;
    --fold: rgba(0, 0, 0, 0.05);
  }
  * { margin: 0; padding: 0; box-sizing: border-box; }
  html, body { width: 1200px; height: 868px; overflow: hidden; background: var(--backdrop); }
  .canvas { position: relative; width: 1200px; height: 868px; }
  .spread {
    position: absolute; left: 80px; top: 44px; width: 1040px; height: 780px;
    background: linear-gradient(90deg, var(--paper-light), var(--paper));
  }
  .spread-shapes { position: absolute; inset: 0; }
  .page { position: absolute; top: 0; width: 520px; height: 780px; }
  .page-back { left: 0; }
  .page-front { left: 520px; }
  .spine-line { position: absolute; left: 519px; top: 0; width: 2px; height: 780px; background: var(--fold); }

  .back-name {
    position: absolute; left: 0; width: 520px; top: 300px; text-align: center;
    font-family: "Lato", sans-serif; font-weight: 700; font-size: 30px;
    color: var(--magenta); letter-spacing: 1px;
  }

  .brand-name {
    position: absolute; left: 0; width: 520px; top: 130px; text-align: center;
    font-family: "Lato", sans-serif; font-weight: 700; font-size: 30px;
    color: var(--magenta); letter-spacing: 0.5px;
  }

  .year {
    position: absolute; left: 0; width: 520px; top: 215px; text-align: center;
    font-family: "Lato", sans-serif; font-weight: 900; font-size: 110px;
    color: var(--numeral); line-height: 1;
  }
  .confidential {
    position: absolute; left: 0; width: 520px; top: 338px; text-align: center;
    font-family: "Lato", sans-serif; font-weight: 400; font-size: 10px;
    letter-spacing: 3px; color: var(--magenta);
  }
  .flower-art {
    position: absolute; left: 250px; top: 370px; width: 80px; height: 150px;
    border-radius: 40px 40px 8px 8px;
    background: linear-gradient(180deg, rgba(220,114,153,0.28), rgba(220,114,153,0.06));
  }
  .cover-title {
    position: absolute; left: 0; width: 520px; top: 650px; text-align: center;
    font-family: "Caveat", cursive; font-weight: 500; font-size: 34px; color: var(--white);
  }
</style>
</head>
<body>
<main class="canvas">
  <section class="spread">
    <svg class="spread-shapes" viewBox="0 0 1040 780" width="1040" height="780" aria-hidden="true">
      <path class="band-pink" fill="var(--pink-band)"
        d="M0 672 C180 640 380 590 520 545 C700 500 880 470 985 440 C1020 430 1040 400 1040 360 L1040 780 L0 780 Z"/>
      <path class="band-magenta" fill="var(--magenta)"
        d="M0 688 C180 656 380 606 520 561 C700 516 880 486 990 456 C1024 446 1040 420 1040 384 L1040 780 L0 780 Z"/>
    </svg>
    <div class="spine-line"></div>

    <article class="page page-back">
      <p class="back-name">Meridian Ascent</p>
    </article>

    <article class="page page-front">
      <p class="brand-name">SUMMIT RISE</p>
      <p class="year">2022</p>
      <p class="confidential">CONFIDENTIAL</p>
      <div class="flower-art" role="img" aria-label="Fine line drawing of a single daisy on a slender stem"></div>
      <p class="cover-title">A year in Review</p>
    </article>
  </section>
</main>
</body>
</html>
```